CSS Template Layout

We are looking for a page design template that we can update our site. Here are the requirements.

We need a header image across the top and three columns below. Layout should be controlled by css, not tables.

This is for a landscape/snow removal directory. A generic layout for overall size can be found at www.brindlemowpath.net Images should relate to lawns/landscaping/snow removal.

We do not have a logo at this time, so we will simply be using a font with the site name. The site should be colorful and inviting, it should feel fresh and clean. These are landscapers and they groom the beauty found in nature.

Do not hesitate to ask questions or bounce ideas off of us.

Project Deadline Extended
Reason: We are sorry but we need to extend the deadline, we inadvertently deadlined on a Saturday and will not be in the office. We have internally worked out our schedules to meet next thursday. On the plus side, we are guaranteeing payment based on the two designs submitted already.

```html
<!DOCTYPE html>
<html lang="en">
<head>
<meta charset="utf-8">
<title>Brindle Mowpath – Landscape Service Directory</title>
<link rel="stylesheet" href="https://fonts.googleapis.com/css2?family=Roboto:wght@300;400;500;700&display=swap">
<style>
  :root {
    --page-bg: #f9f9f9;
    --panel-bg: #ffffff;
    --side-bg: #f3f3f3;
    --ink: #5e5e5e;
    --ink-soft: #777777;
    --green: #82a632;
    --green-light: #93b64a;
    --green-dark: #6a8d24;
    --green-button: #66881f;
    --grey-button: #717171;
    --rule: #d9d9d9;
    --footer: #6b6b6b;
    --ad-bg: #e9e9e9;
    --ad-ink: #d4d4d4;
  }
  * { box-sizing: border-box; margin: 0; padding: 0; }
  html, body { width: 1200px; height: 1000px; overflow: hidden; }
  body {
    position: relative;
    background: var(--page-bg);
    font-family: "Roboto", "Helvetica Neue", Arial, sans-serif;
    font-weight: 300;
    color: var(--ink);
  }
  a { color: inherit; text-decoration: none; }

  /* Header */
  .site-header { position: absolute; left: 0; top: 0; width: 1200px; height: 107px; }
  .site-title { position: absolute; left: 127px; top: 22px; font-size: 33px; font-weight: 300; color: #5a5a5a; letter-spacing: -0.3px; }
  .site-tagline { position: absolute; left: 129px; top: 65px; font-size: 12.5px; color: #6a6a6a; }
  .btn { position: absolute; top: 11px; width: 97px; height: 34px; color: #fff; font-size: 17px; font-weight: 400; display: flex; align-items: center; justify-content: center; border: 1px solid rgba(0,0,0,.25); }
  .btn-signup { left: 857px; background: var(--green-button); }
  .btn-login { left: 972px; background: var(--grey-button); }
  .search { position: absolute; left: 713px; top: 55px; width: 356px; height: 37px; background: #e4e4e4; border-radius: 6px; padding: 5px; display: flex; }
  .search-field { flex: 1; background: #fff; border: 1px solid #d6d6d6; border-right: none; display: flex; align-items: center; padding-left: 6px; font-size: 11.5px; color: #b5b5b5; gap: 6px; }
  .search-button { width: 58px; background: #fff; border: 1px solid #d6d6d6; font-size: 11.5px; font-weight: 500; color: #666; display: flex; align-items: center; justify-content: center; }

  /* Navigation */
  .main-nav { position: absolute; left: 0; top: 107px; width: 1200px; height: 61px; background: var(--green); border-top: 2px solid var(--green-dark); border-bottom: 4px solid var(--green-dark); }
  .main-nav ul { list-style: none; position: absolute; left: 130px; top: 0; height: 55px; display: flex; }
  .main-nav li { height: 55px; display: flex; align-items: center; justify-content: center; color: #fff; font-size: 18px; font-weight: 300; }
  .main-nav li.is-active { background: var(--green-light); font-weight: 500; }

  /* Content panel */
  .content-panel { position: absolute; left: 130px; top: 168px; width: 683px; height: 789px; background: var(--panel-bg); }
  .side-strip { position: absolute; left: 139px; top: 194px; width: 142px; height: 736px; background: var(--side-bg); }
  .social { position: absolute; left: 163px; top: 214px; display: flex; gap: 14px; }
  .social span { width: 22px; height: 22px; display: block; }
  .thumb { position: absolute; left: 174px; width: 71px; height: 41px; border: 1px solid #e0e0e0; }

  .section-title { position: absolute; font-size: 24px; font-weight: 400; color: #666; }
  .rule { position: absolute; height: 1px; background: var(--rule); }
  .intro-box { position: absolute; left: 294px; top: 252px; width: 504px; height: 70px; background: #f1f1f1; border-bottom: 1px solid #e2e2e2; padding: 14px 12px; font-size: 15.5px; line-height: 20px; color: #7a7a7a; }
  .category { position: absolute; font-size: 19.5px; color: #5e5e5e; }

  .listing-card { position: absolute; left: 298px; width: 221px; background: #fff; box-shadow: 0 1px 4px rgba(0,0,0,.2); display: flex; align-items: center; justify-content: center; gap: 8px; }
  .listing-mark-name { font-size: 17px; font-weight: 500; }
  .listing-info { position: absolute; text-align: center; }
  .listing-name { font-size: 19.5px; color: #555; line-height: 24px; }
  .listing-desc { font-size: 12.5px; color: #666; line-height: 16px; margin-top: 6px; }

  /* Right column */
  .side-menu { position: absolute; left: 821px; top: 246px; list-style: none; }
  .side-menu li { height: 35.7px; display: flex; align-items: center; font-size: 15.5px; color: #6a6a6a; }
  .side-menu svg { margin-left: 2px; margin-right: 27px; }
  .ad-slot { position: absolute; left: 822px; top: 680px; width: 248px; height: 260px; background: var(--ad-bg); display: flex; align-items: center; justify-content: center; font-size: 22px; font-weight: 700; color: var(--ad-ink); letter-spacing: .3px; }

  /* Footer */
  .site-footer { position: absolute; left: 0; top: 957px; width: 1200px; height: 43px; background: var(--footer); border-top: 2px solid #5a5a5a; color: #fff; font-size: 12.5px; }
  .footer-links { position: absolute; left: 129px; top: 13px; display: flex; }
  .footer-links span + span::before { content: "|"; margin: 0 7px; }
  .copyright { position: absolute; right: 130px; top: 13px; }
</style>
</head>
<body>
  <header class="site-header">
    <h1 class="site-title">Brindle Mowpath</h1>
    <p class="site-tagline">An organized landscape service directory</p>
    <a class="btn btn-signup" href="#">Signup</a>
    <a class="btn btn-login" href="#">Login</a>
    <form class="search">
      <div class="search-field">
        <svg width="14" height="14" viewBox="0 0 14 14"><circle cx="5.5" cy="5.5" r="4" fill="none" stroke="#444" stroke-width="2"/><line x1="8.5" y1="8.5" x2="13" y2="13" stroke="#444" stroke-width="2.4"/></svg>
        e.g. Service type or company name
      </div>
      <div class="search-button">Search</div>
    </form>
  </header>

  <nav class="main-nav">
    <ul>
      <li class="is-active" style="width:103px">Home</li>
      <li style="width:233px">Landscape Service</li>
      <li style="width:156px">Lawn Service</li>
      <li style="width:200px">Snow Removal</li>
      <li style="width:125px">Advertise</li>
      <li style="width:143px">Contact</li>
    </ul>
  </nav>

  <main class="content-panel"></main>

  <aside class="side-strip"></aside>
  <div class="social">
    <span role="img" aria-label="Social network link" style="background:#3b5a97"></span>
    <span role="img" aria-label="Social network link" style="background:#dfe6ea;border:1px solid #c4cdd2"></span>
    <span role="img" aria-label="Social network link" style="background:#1f76b4"></span>
  </div>
  <div class="thumb" role="img" aria-label="Landscaping photo" style="top:265px;background:linear-gradient(160deg,#f2f2f2,#9a9a9a)"></div>
  <div class="thumb" role="img" aria-label="Lawn care photo" style="top:324px;background:linear-gradient(160deg,#8a8a8a,#3c3c3c)"></div>
  <div class="thumb" role="img" aria-label="Snow removal photo" style="top:384px;background:linear-gradient(100deg,#c9e6f5 0%,#c9e6f5 30%,#4a4a4a 32%,#3a3a3a)"></div>

  <h2 class="section-title" style="left:292px;top:190px">Browse Businesses</h2>
  <div class="rule" style="left:292px;top:234px;width:506px"></div>
  <p class="intro-box">View the listings below or submit your website to be entered into our directoy.</p>
  <a class="category" href="#" style="left:294px;top:354px">Landscape Service (2)</a>
  <a class="category" href="#" style="left:296px;top:410px">Lawn Services (2)</a>
  <a class="category" href="#" style="left:294px;top:467px">Snow Removal Service (1)</a>
  <a class="category" href="#" style="left:294px;top:523px">Tree Service (1)</a>

  <h2 class="section-title" style="left:292px;top:634px">Featured Listings</h2>
  <div class="rule" style="left:292px;top:679px;width:506px"></div>

  <div class="listing-card" style="top:709px;height:89px">
    <span class="listing-mark-name" style="color:#2a62c9">Meadowline Lawn Care</span>
  </div>
  <div class="listing-info" style="left:530px;top:736px;width:270px">
    <div class="listing-name">Meadowline Lawn Care</div>
    <div class="listing-desc" style="margin-top:4px">Rivertons Premier Landscaping Company</div>
  </div>

  <div class="listing-card" style="top:829px;height:101px">
    <span style="width:14px;height:14px;border-radius:50%;background:#2f5fb3;display:block"></span>
    <span class="listing-mark-name" style="color:#2f5fb3">Hollis Landscape</span>
  </div>
  <div class="listing-info" style="left:552px;top:842px;width:256px">
    <div class="listing-name">Hollis Landscape Services, Inc.</div>
    <div class="listing-desc">We are a full service landscape maintenance company</div>
  </div>

  <h2 class="section-title" style="left:821px;top:192px">Menu</h2>
  <div class="rule" style="left:821px;top:234px;width:249px"></div>
  <ul class="side-menu">
    <li><svg width="8" height="14" viewBox="0 0 8 14"><polygon points="0,0 8,7 0,14" fill="#b5b5b5"/></svg>Menu Item 1</li>
    <li><svg width="8" height="14" viewBox="0 0 8 14"><polygon points="0,0 8,7 0,14" fill="#b5b5b5"/></svg>Menu Item 2</li>
    <li><svg width="8" height="14" viewBox="0 0 8 14"><polygon points="0,0 8,7 0,14" fill="#b5b5b5"/></svg>Menu Item 3</li>
    <li><svg width="8" height="14" viewBox="0 0 8 14"><polygon points="0,0 8,7 0,14" fill="#b5b5b5"/></svg>Menu Item 4</li>
  </ul>
  <div class="ad-slot">ADVERTISEMENT</div>

  <footer class="site-footer">
    <div class="footer-links">
      <span>Home</span><span>Landscape Service</span><span>Lawn Service</span><span>Snow Removal</span><span>Advertise</span><span>Contact</span>
    </div>
    <div class="copyright">©Copyright 2013 Brindle Mowpath</div>
  </footer>
</body>
</html>
```